Card design for Heating and Cooling company

this is for a heating and cooling company we recently updated our logo and need to update our cards. We attached our logo so you can incorporate it into the card. We specialize in residential and commercial furnace and air condition repairs. Have been in business since 2014.

Phone number 555.284.9137

We need the following phrases
:Repairs, Installations, and maintenance
:Quality work at reasonable prices
:residential/commercial
:Licensed &Insured
:Email Pinegrovehvac47@mailbox-example.com
Name: Teodor K (Ted)
Also on back side I would like my logo with wording :Thank you for your business and refferal

Industry/Entity Type

Hvac

Contact Information for Business Card

:residential/commercial
:Licensed & Insured
Name: Teodor K (Ted)
Number:555.284.9136

Requirements
Must have
• Blue and red colors
Nice to have
• Maybe a pic of a furnace or air conditioner

```html
<!DOCTYPE html>
<html lang="en">
<head>
<meta charset="utf-8">
<title>Heating and Cooling Business Card</title>
<link href="https://fonts.googleapis.com/css2?family=Arimo:wght@700&display=swap" rel="stylesheet">
<style>
  :root {
    --red: #e8202a;
    --orange: #f47b20;
    --amber: #fbb01f;
    --steel: #9fb3b8;
    --sky: #35a6e0;
    --ink: #0a0a0a;
    --white: #ffffff;
  }
  * { margin: 0; padding: 0; box-sizing: border-box; }
  html, body {
    width: 1200px;
    height: 686px;
    overflow: hidden;
    background: var(--white);
  }
  .card {
    position: relative;
    width: 1200px;
    height: 686px;
    overflow: hidden;
    font-family: "Arimo", Arial, sans-serif;
    font-weight: 700;
    text-transform: uppercase;
    color: var(--ink);
    background: linear-gradient(to top right,
      var(--red) 0%,
      var(--red) 22%,
      var(--orange) 40%,
      var(--amber) 54%,
      var(--steel) 66%,
      var(--sky) 80%,
      var(--sky) 100%);
  }
  .services {
    list-style: none;
  }
  .service {
    position: absolute;
    right: 66px;
    display: flex;
    align-items: center;
    font-size: 36px;
    line-height: 1;
    white-space: nowrap;
  }
  .service-ring {
    display: inline-block;
    width: 19px;
    height: 19px;
    border: 4px solid var(--white);
    border-radius: 50%;
    margin-right: 20px;
    flex: none;
  }
  .service-1 { top: 75px; }
  .service-2 { top: 144px; }
  .service-3 { top: 212px; }
  .service-4 { top: 281px; }

  .divider {
    position: absolute;
    left: 65px;
    top: 354px;
    width: 301px;
    height: 19px;
    background: var(--ink);
  }
  .contact-line {
    position: absolute;
    left: 65px;
    line-height: 1;
    white-space: nowrap;
  }
  .contact-name { top: 420px; font-size: 60px; }
  .contact-label { color: var(--white); }
  .contact-email { top: 509px; font-size: 44px; }
  .email-dot { color: var(--amber); }
  .contact-phone { top: 572px; font-size: 60px; color: var(--white); }
</style>
</head>
<body>
  <div class="card">
    <ul class="services">
      <li class="service service-1"><span class="service-ring"></span>Repairs, Installations and Maintenance</li>
      <li class="service service-2"><span class="service-ring"></span>Quality Work at Reasonable Prices</li>
      <li class="service service-3"><span class="service-ring"></span>Residential and Commercial</li>
      <li class="service service-4"><span class="service-ring"></span>Licensed and Insured</li>
    </ul>

    <div class="divider"></div>

    <p class="contact-line contact-name"><span class="contact-label">Contact</span> Teodor K (“Ted”)</p>
    <p class="contact-line contact-email">Pinegrovehvac47@mailbox-example<span class="email-dot">.</span>com</p>
    <p class="contact-line contact-phone">555.284.9137</p>
  </div>
</body>
</html>
```